Accommodation business card design

We need a business card designed for our long-term accommodation business based in Australia. The business card must match the style of the attached letterhead and logo. The same contact details that are on the letterhead will also go on the card except that the card must list the contact details in the following order:phone, email, home address, ABN.

The card will be printed on .76mm white pvc plastic (same as credit cards), printed both sides and will be silver foil stamped on at least one side (preferably 2 sides) The design template is attached, but please go to www.zt.com.au for more specs.

The only other addition the card will be my name: Malcolm Darby

```html
<!DOCTYPE html>
<html lang="en">
<head>
<meta charset="utf-8">
<title>Summit Lodgings – Business Card</title>
<link rel="stylesheet" href="https://fonts.googleapis.com/css2?family=Open+Sans:wght@400;600;800&display=swap">
<style>
  :root {
    --bg: #eceef2;
    --card: #ffffff;
    --brown: #8c4a3f;
    --maroon: #6c1a3a;
    --ink: #2f2f2f;
    --shadow: rgba(40, 40, 60, 0.18);
  }
  * { margin: 0; padding: 0; box-sizing: border-box; }
  html, body {
    width: 1200px; height: 987px; overflow: hidden;
    background: var(--bg);
    font-family: "Open Sans", Arial, sans-serif;
  }
  .stage { position: relative; width: 1200px; height: 987px; }
  .card {
    position: absolute;
    width: 560px; height: 353px;
    background: var(--card);
    border-radius: 26px;
    overflow: hidden;
    box-shadow: 0 10px 30px var(--shadow);
  }
  .card--front { left: 30px; top: 317px; }
  .card--back { left: 610px; top: 317px; }

  .brand { position: absolute; display: flex; align-items: center; gap: 16px; }
  .brand__mark { width: 70px; height: 70px; border-radius: 12px; background: var(--maroon); flex: none; }
  .brand__name {
    color: var(--brown); font-weight: 800; text-transform: uppercase;
    line-height: 1; letter-spacing: 0.5px;
  }
  .card--front .brand { left: 34px; top: 26px; }
  .card--front .brand__name { font-size: 34px; }

  .contact { position: absolute; left: 40px; top: 112px; list-style: none; color: var(--ink); font-size: 14px; }
  .contact li { display: flex; align-items: center; gap: 8px; height: 24px; }
  .contact svg { width: 14px; height: 14px; flex: none; fill: var(--brown); }

  .wave { position: absolute; inset: 0; width: 100%; height: 100%; }
  .holder-name {
    position: absolute; right: 30px; bottom: 12px;
    color: #fff; font-weight: 600; font-size: 24px; line-height: 1.2;
  }

  .card--back .brand { left: 0; right: 0; top: 110px; justify-content: center; }
  .card--back .brand__name { font-size: 44px; text-align: center; }
  .web {
    position: absolute; left: 0; right: 0; top: 250px; text-align: center;
    color: var(--ink); font-size: 16px; letter-spacing: 5px;
  }
</style>
</head>
<body>
<main class="stage">
  <section class="card card--front" aria-label="Card front">
    <svg class="wave" viewBox="0 0 560 353" aria-hidden="true">
      <path d="M0,225 C150,268 340,292 560,286 L560,353 L0,353 Z" fill="var(--maroon)"/>
      <path d="M0,242 C150,288 340,306 560,300 L560,353 L0,353 Z" fill="var(--brown)"/>
      <path d="M0,229 C110,260 240,284 380,290 C240,289 110,270 0,238 Z" fill="#fff"/>
    </svg>
    <div class="brand">
      <span class="brand__mark"></span>
      <span class="brand__name">Summit<br>Lodgings</span>
    </div>
    <ul class="contact">
      <li><svg viewBox="0 0 24 24"><path d="M6.6 10.8a15.1 15.1 0 0 0 6.6 6.6l2.2-2.2a1 1 0 0 1 1-.25 11.4 11.4 0 0 0 3.6.57 1 1 0 0 1 1 1V20a1 1 0 0 1-1 1A17 17 0 0 1 3 4a1 1 0 0 1 1-1h3.5a1 1 0 0 1 1 1c0 1.25.2 2.45.57 3.57a1 1 0 0 1-.25 1z"/></svg>0438 617 204</li>
      <li><svg viewBox="0 0 24 24"><path d="M2 5h20v14H2z M4 7v1l8 5 8-5V7l-8 5z" fill-rule="evenodd"/></svg>malcolmdarby@mailbox.com</li>
      <li><svg viewBox="0 0 24 24"><path d="M12 3 2 11h3v9h5v-6h4v6h5v-9h3z"/></svg>PO Box 3187, Bowen Mail Centre, QLD 4805</li>
      <li>ABN 51 482 907 316</li>
    </ul>
    <p class="holder-name">Malcolm Darby</p>
  </section>

  <section class="card card--back" aria-label="Card back">
    <div class="brand">
      <span class="brand__name">Summit<br>Lodgings</span>
    </div>
    <p class="web">www.zt.com.au</p>
  </section>
</main>
</body>
</html>
```